Massage therapist LMT

I need something simple and beautiful I'm a man no flowers, no leafs,no tree please

Target Market(s)

People who suffer ( body pain,stess,body injury ect.. )

Industry/Entity Type

Massage Therapy

Contact Information for Business Card

Marcus T Abernathy LMT

Font styles to use
Serif
Script

Colors

Designer to choose colors to be used in the design.

Requirements
Must have
• Get a massage
• For the
• Health
• Of it
Nice to have
• Skeleton
Should not have
• No flowers
• No tree

```html
<!DOCTYPE html>
<html lang="en">
<head>
<meta charset="utf-8">
<title>Marcus T Abernathy LMT – Business Card</title>
<link rel="stylesheet" href="https://fonts.googleapis.com/css2?family=Yellowtail&family=Tinos:wght@400;700&display=swap">
<style>
  :root {
    --page-bg: #2a2a2a;
    --card-red: #9b1c1f;
    --ink-light: #ffffff;
    --muscle-light: #e8ae9a;
    --muscle-mid: #d0806a;
  }
  * { margin: 0; padding: 0; box-sizing: border-box; }
  html, body {
    width: 1200px; height: 880px; overflow: hidden;
    background: var(--page-bg);
  }
  .stage {
    width: 1200px; height: 880px;
    display: flex; flex-direction: column;
    align-items: center; justify-content: center; gap: 40px;
  }
  .card {
    position: relative;
    width: 640px; height: 366px;
    background: var(--card-red);
    border-radius: 18px;
    overflow: hidden;
    color: var(--ink-light);
  }
  .brand {
    display: flex; flex-direction: column;
  }
  .brand-name {
    font-family: "Yellowtail", "Brush Script MT", "Segoe Script", cursive;
    font-weight: 400;
    color: var(--ink-light);
    white-space: nowrap;
    line-height: 1.1;
  }
  .brand-title {
    font-family: "Tinos", "Times New Roman", serif;
    color: var(--ink-light);
    letter-spacing: 1px;
    line-height: 1;
  }

  /* Front */
  .card-front .brand {
    position: absolute; left: 0; right: 0; top: 128px;
    align-items: center;
  }
  .card-front .brand-name { font-size: 60px; }
  .card-front .brand-title {
    font-size: 18px; margin-top: 4px; margin-left: 60px;
  }

  /* Back */
  .anatomy-art {
    position: absolute; left: 0; top: 0; width: 640px; height: 366px;
  }
  .card-back .brand {
    position: absolute; right: 34px; top: 30px;
    align-items: flex-end;
  }
  .card-back .brand-name { font-size: 44px; }
  .card-back .brand-title { font-size: 15px; margin-top: 6px; }

  .contact {
    position: absolute; left: 400px; top: 150px;
    font-family: "Tinos", "Times New Roman", serif;
    font-size: 13px; line-height: 1.3;
    color: var(--ink-light);
  }
  .contact-name { font-weight: 700; font-size: 15px; letter-spacing: 0.5px; }
  .contact-role { font-size: 12px; margin-bottom: 10px; }
  .contact-address { margin-bottom: 10px; }
  .contact-line { display: flex; align-items: center; gap: 8px; margin-bottom: 3px; }
  .contact-icon { width: 16px; height: 16px; flex: none; }
</style>
</head>
<body>
<main class="stage">

  <section class="card card-front">
    <div class="brand">
      <span class="brand-name">Marcus T Abernathy</span>
      <span class="brand-title">LMT</span>
    </div>
  </section>

  <section class="card card-back">
    <svg class="anatomy-art" viewBox="0 0 640 366" role="img" aria-label="Illustration of a human torso and outstretched arm showing muscle anatomy">
      <defs>
        <radialGradient id="muscleTone" cx="0.12" cy="0.95" r="0.75">
          <stop offset="0" stop-color="var(--muscle-light)"/>
          <stop offset="0.45" stop-color="var(--muscle-mid)" stop-opacity="0.85"/>
          <stop offset="1" stop-color="var(--muscle-mid)" stop-opacity="0"/>
        </radialGradient>
      </defs>
      <rect x="0" y="60" width="400" height="306" fill="url(#muscleTone)"/>
    </svg>

    <div class="brand">
      <span class="brand-name">Marcus T Abernathy</span>
      <span class="brand-title">LMT</span>
    </div>

    <div class="contact">
      <div class="contact-name">DANIEL REEVE</div>
      <div class="contact-role">Founder</div>
      <div class="contact-address">PO BOX 456 Harbor Lane<br>5th street Ashford</div>
      <div class="contact-line">
        <svg class="contact-icon" viewBox="0 0 16 16" aria-hidden="true"><circle cx="8" cy="8" r="7.3" fill="none" stroke="#fff" stroke-width="1.2"/><rect x="5.5" y="3.5" width="5" height="9" rx="1" fill="none" stroke="#fff" stroke-width="1.1"/></svg>
        <span>(555) 210-3344</span>
      </div>
      <div class="contact-line">
        <svg class="contact-icon" viewBox="0 0 16 16" aria-hidden="true"><circle cx="8" cy="8" r="7.3" fill="none" stroke="#fff" stroke-width="1.2"/><rect x="4" y="5" width="8" height="6" fill="none" stroke="#fff" stroke-width="1.1"/><path d="M4 5 L8 8.5 L12 5" fill="none" stroke="#fff" stroke-width="1.1"/></svg>
        <span>hello@abernathymassage.com</span>
      </div>
      <div class="contact-line">
        <svg class="contact-icon" viewBox="0 0 16 16" aria-hidden="true"><circle cx="8" cy="8" r="7.3" fill="none" stroke="#fff" stroke-width="1.2"/><circle cx="8" cy="8" r="4.2" fill="none" stroke="#fff" stroke-width="1"/><path d="M3.8 8 H12.2 M8 3.8 C6 6 6 10 8 12.2 M8 3.8 C10 6 10 10 8 12.2" fill="none" stroke="#fff" stroke-width="0.9"/></svg>
        <span>www.abernathymassage.com</span>
      </div>
    </div>
  </section>

</main>
</body>
</html>
```